Design for signage on vans

I have purchased two new Corvane Trekker vans and i would like them designed so that there is brand synergy with our website etc.

our website is www.brivolink.ie

```html
<!DOCTYPE html>
<html lang="en">
<head>
<meta charset="utf-8">
<title>Brivolink – Corvane Trekker van livery</title>
<link rel="stylesheet" href="https://fonts.googleapis.com/css2?family=Montserrat:ital,wght@0,500;0,700;1,800&display=swap">
<style>
  :root {
    --navy: #1f3550;
    --navy-deep: #142437;
    --navy-ray: #2b4666;
    --red: #d8322b;
    --red-dark: #c2271f;
    --white: #ffffff;
    --phone-grey: #eceff2;
    --glass: #5d6166;
    --trim: #222427;
    --hub: #a9adb2;
    --page: #ffffff;
  }
  html, body {
    margin: 0;
    padding: 0;
    width: 1200px;
    height: 1106px;
    overflow: hidden;
    background: var(--page);
  }
  .livery-sheet { display: block; width: 1200px; height: 1106px; }
  .brand-name { font-family: "Montserrat", sans-serif; font-weight: 500; fill: var(--white); }
  .brand-tagline { font-family: "Montserrat", sans-serif; font-weight: 500; fill: var(--white); }
  .phone-number { font-family: "Montserrat", sans-serif; font-weight: 800; font-style: italic; fill: var(--phone-grey); }
  .web-address { font-family: "Montserrat", sans-serif; font-weight: 700; fill: var(--white); }
  .brand-dot { fill: none; stroke: var(--white); stroke-width: 9; }
</style>
</head>
<body>
<svg class="livery-sheet" viewBox="0 0 2000 1843" xmlns="http://www.w3.org/2000/svg">
  <defs>
    <path id="body-outline" d="M120,560 L160,460 Q230,420 470,385 L790,175 Q900,150 1060,150 L1795,150 Q1850,155 1862,300 L1878,600 L1925,640 L1925,715 L1765,728 A150,150 0 0 0 1480,735 L565,742 A150,150 0 0 0 280,742 L115,712 Z"/>
    <clipPath id="body-clip"><use href="#body-outline"/></clipPath>
    <radialGradient id="panel-glow" cx="0.55" cy="0.45" r="0.6">
      <stop offset="0" stop-color="var(--navy-ray)"/>
      <stop offset="1" stop-color="var(--navy)"/>
    </radialGradient>
    <g id="van-livery">
      <use href="#body-outline" fill="var(--navy)"/>
      <g clip-path="url(#body-clip)">
        <rect class="rear-panel-burst" role="img" aria-label="Soft sunburst texture behind the brand name" x="1040" y="150" width="840" height="310" fill="url(#panel-glow)"/>
        <path class="stripe-white" d="M1880,460 L860,460 Q730,460 690,560 L585,745 L655,745 L760,535 Q790,486 870,486 L1880,486 Z" fill="var(--white)"/>
        <path class="band-red" d="M1880,496 L885,496 Q812,496 782,560 L668,745 L1880,745 Z" fill="var(--red)"/>
        <path class="band-shade" d="M702,690 L1880,690 L1880,745 L668,745 Z" fill="var(--red-dark)"/>
      </g>
      <path class="windscreen" d="M500,388 L770,215 L720,300 L610,410 Z" fill="var(--trim)"/>
      <path class="cab-window" d="M625,280 Q650,235 720,222 L1000,210 L1000,400 L625,415 Z" fill="var(--glass)"/>
      <path class="rub-strip" d="M700,640 Q710,620 740,618 L1250,608 Q1290,612 1290,650 L1285,668 L705,685 Z" fill="var(--trim)"/>
      <path class="front-bumper" d="M118,560 L205,558 L205,740 L112,712 Z" fill="var(--trim)"/>
      <path class="rear-bumper" d="M1770,595 L1895,598 Q1930,620 1925,690 L1900,725 L1765,728 Z" fill="var(--trim)"/>
      <rect class="tail-light" x="1852" y="380" width="24" height="140" rx="8" fill="var(--red-dark)"/>
      <g class="wheel">
        <circle cx="420" cy="722" r="130" fill="var(--trim)"/>
        <circle cx="420" cy="722" r="78" fill="var(--hub)"/>
        <circle cx="420" cy="722" r="24" fill="var(--trim)"/>
      </g>
      <g class="wheel">
        <circle cx="1625" cy="722" r="130" fill="var(--trim)"/>
        <circle cx="1625" cy="722" r="78" fill="var(--hub)"/>
        <circle cx="1625" cy="722" r="24" fill="var(--trim)"/>
      </g>
    </g>
  </defs>

  <g class="van van-left-side">
    <use href="#van-livery"/>
    <g class="brand-lockup">
      <circle class="brand-dot" cx="1225" cy="293" r="72"/>
      <text class="brand-name" x="1318" y="288" font-size="86">Brivolink</text>
      <text class="brand-tagline" x="1318" y="370" font-size="70">IT Solutions</text>
    </g>
    <text class="phone-number" x="830" y="570" font-size="50">045 318264</text>
    <g class="web-pill">
      <path d="M1185,530 L1502,530 L1502,577 L1168,577 Z" fill="var(--navy-deep)"/>
      <text class="web-address" x="1196" y="565" font-size="30">www.brivolink.ie</text>
    </g>
  </g>

  <g class="van van-right-side">
    <use href="#van-livery" transform="translate(2000,873) scale(-1,1)"/>
    <g class="brand-lockup">
      <circle class="brand-dot" cx="392" cy="1166" r="72"/>
      <text class="brand-name" x="485" y="1161" font-size="86">Brivolink</text>
      <text class="brand-tagline" x="485" y="1243" font-size="70">IT Solutions</text>
    </g>
    <g class="web-pill">
      <path d="M512,1403 L828,1403 L834,1450 L495,1450 Z" fill="var(--navy-deep)"/>
      <text class="web-address" x="514" y="1438" font-size="30">www.brivolink.ie</text>
    </g>
    <text class="phone-number" x="858" y="1443" font-size="50">045 318264</text>
  </g>
</svg>
</body>
</html>
```